Copper Vale Winery wants innovative label for unique bottling

We are looking for a lable for a champagne which is made of Eiswein (Ice Wine; this is what you get when you harvest the grapes at temperatures below -7 degrees celsius. the water is frozen and you only get the pure extract out of the grapes (sugar, acid and all the aromas). even after fermentation is remains very sweet. we then turned it into champagne (2nd fermentation in bottles for another 12 months and so on and so forth). It is bottled in small champagne bottles (0,375 l). Dark green (just like a champagne bottle). The name of the product is "Glintova" (from Freeze and Riesling). So it is unique, it is sparkling, it is sweet, it is full of aromas and it is produced from deep frozen grapes. All of this hopefully creates ideas in your imagination which lead to great designs! The only word printed onto the label is "Glintova". The colour code should still be recognizable. See www.brandt-wolmer.de for our standard labels and bottles. you can also download label designs and colours. we prefer modern / fresh / light design rather than traditional, flowery, pittoresque. But please not 100 different colours or screaming colours. You may also imagine transparent labels. Up to you! Have fun!

```html
<!DOCTYPE html>
<html lang="en">
<head>
<meta charset="utf-8">
<title>Glintova – Label</title>
<link href="https://fonts.googleapis.com/css2?family=Bodoni+Moda:opsz,wght@6..96,400&display=swap" rel="stylesheet">
<style>
  :root {
    --page-bg: #f4f5f6;
    --label-slate-light: #2d3d48;
    --label-slate-dark: #182228;
    --ice-white: #f3f5f6;
    --glacier-deep: #1b4e78;
    --glacier-mid: #2c7fb2;
    --glacier-light: #8cc4d9;
    --snow-grey: #b9c3c8;
  }
  html, body {
    margin: 0;
    padding: 0;
    width: 1200px;
    height: 2487px;
    overflow: hidden;
    background: var(--page-bg);
  }
  .canvas {
    position: relative;
    width: 1200px;
    height: 2487px;
  }
  .label {
    position: absolute;
    left: 80px;
    top: 776px;
    width: 1040px;
    height: 935px;
  }
  .label-shape {
    position: absolute;
    inset: 0;
    width: 100%;
    height: 100%;
  }
  .label-name {
    position: absolute;
    right: 70px;
    top: 352px;
    margin: 0;
    font-family: "Bodoni Moda", "Didot", serif;
    font-weight: 400;
    font-size: 164px;
    line-height: 1;
    letter-spacing: 2px;
    color: var(--ice-white);
  }
  .label-mountains {
    position: absolute;
    left: 0;
    bottom: 0;
    width: 100%;
    height: 365px;
    background:
      linear-gradient(100deg, rgba(255,255,255,0) 0%, rgba(140,196,217,0.35) 35%, rgba(255,255,255,0) 60%, rgba(140,196,217,0.25) 75%, rgba(255,255,255,0) 100%),
      linear-gradient(180deg, var(--label-slate-dark) 0%, var(--snow-grey) 14%, var(--glacier-light) 30%, var(--glacier-mid) 62%, var(--glacier-deep) 100%);
  }
</style>
</head>
<body>
  <main class="canvas">
    <section class="label">
      <svg class="label-shape" viewBox="0 0 1040 935" preserveAspectRatio="none" aria-hidden="true">
        <defs>
          <linearGradient id="slate" x1="0" y1="0" x2="1" y2="1">
            <stop offset="0" stop-color="#2d3d48"/>
            <stop offset="1" stop-color="#182228"/>
          </linearGradient>
        </defs>
        <path d="M0 0 C 330 18, 780 70, 1040 205 L 1040 935 L 0 935 Z" fill="url(#slate)"/>
      </svg>
      <h1 class="label-name">Glintova</h1>
      <div class="label-mountains" role="img" aria-label="Faceted illustration of icy blue mountain peaks with white snowcaps"></div>
    </section>
  </main>
</body>
</html>
```